Advertising poster for podcast event

"The Lantern Table" is one of the most popular podcasts in Switzerland (https://listen.brovakast.example/show/4kqPLmWX317TRvbnQ8ZsHD). It is hosted by the two radio DJs Lukas Brandt and Adrian Furrer. For a series of live shows where the podcast is recorded with an audience, we need a design of a poster. This should have the format A3 high. In addition, the image must be used that was uploaded here, because this is the cover photo with which you can always recognize the podcast. But what is designed around it is up to you. In addition, it must contain the following text:

- Title of the event:
The lantern table - Live
- Show dates:
Saturday, November 11, 2023 - Solothurn
Wednesday, December 27, 2023 - Berne
Thursday, December 28, 2023 - Berne
- A line with additional information about the presale:
The pavilion, information and tickets: www.diekuppel.example

Target Market(s)

Switzerland

Industry/Entity Type

Entertainment

Requirements
Must have
• The attached image and text according to the briefing.

```html
<!DOCTYPE html>
<html lang="en">
<head>
<meta charset="utf-8">
<title>The Lantern Table – Live</title>
<link rel="stylesheet" href="https://fonts.googleapis.com/css2?family=Oswald:wght@400;500;700&display=swap">
<style>
  :root {
    --sun: #f4bc2f;
    --sun-light: #ffca3e;
    --ink: #231f20;
    --flame: #e03a26;
    --paper: #ffffff;
    --portrait-warm: #efc9ad;
    --portrait-cool: #b7c4de;
  }
  html, body {
    margin: 0;
    padding: 0;
    overflow: hidden;
  }
  .poster {
    position: relative;
    width: 849px;
    height: 1200px;
    overflow: hidden;
    background: radial-gradient(circle at 50% 40%, var(--sun-light) 0%, var(--sun) 70%);
    font-family: "Oswald", "Arial Narrow", sans-serif;
  }
  .presale-line {
    position: absolute;
    top: 68px;
    right: 71px;
    margin: 0;
    font-size: 8.5px;
    font-weight: 400;
    color: var(--ink);
    letter-spacing: 0.1px;
  }
  .presale-line strong {
    font-weight: 700;
  }
  .artwork {
    position: absolute;
    inset: 0;
    width: 849px;
    height: 1200px;
  }
  .event-title {
    font-family: "Oswald", "Arial Narrow", sans-serif;
    font-weight: 700;
    font-size: 80px;
    fill: var(--ink);
  }
  .event-title .live {
    fill: var(--flame);
  }
  .show-date {
    font-family: "Oswald", "Arial Narrow", sans-serif;
    font-weight: 500;
    font-size: 11px;
    fill: var(--paper);
  }
  .show-date .city {
    fill: var(--flame);
  }
</style>
</head>
<body>
<main class="poster">
  <p class="presale-line">The pavilion, information and tickets → <strong>www.diekuppel.example</strong></p>

  <svg class="artwork" viewBox="0 0 849 1200" xmlns="http://www.w3.org/2000/svg">
    <defs>
      <linearGradient id="portrait-tone" x1="0" y1="0" x2="1" y2="1">
        <stop offset="0" stop-color="var(--paper)"/>
        <stop offset="0.55" stop-color="var(--portrait-warm)"/>
        <stop offset="1" stop-color="var(--portrait-cool)"/>
      </linearGradient>
    </defs>

    <g class="speech-bubble">
      <path d="M362 672 L344 790 Q430 768 492 700 Z" fill="var(--ink)"/>
      <circle cx="426" cy="423" r="271" fill="var(--ink)"/>
      <circle class="cover-portrait" cx="426" cy="423" r="248" fill="url(#portrait-tone)"
              role="img" aria-label="Podcast cover illustration: two cheerful cartoon hosts, one giving a thumbs up"/>
    </g>

    <g class="event-title" transform="rotate(-7 425 880)">
      <text x="190" y="880">THE LANTERN</text>
      <text x="262" y="962">TABLE<tspan dx="8" font-weight="400">→</tspan><tspan class="live" dx="6">LIVE</tspan></text>
    </g>

    <g class="show-dates">
      <g transform="translate(186 1093) rotate(-9)">
        <rect x="-116" y="-27" width="232" height="54" rx="27" fill="var(--ink)"/>
        <text class="show-date" x="0" y="4" text-anchor="middle">Thursday, December 28, 2023 → <tspan class="city">Berne</tspan></text>
      </g>
      <g transform="translate(424 1093) rotate(-9)">
        <rect x="-116" y="-27" width="232" height="54" rx="27" fill="var(--ink)"/>
        <text class="show-date" x="0" y="4" text-anchor="middle">Wednesday, December 27, 2023 → <tspan class="city">Berne</tspan></text>
      </g>
      <g transform="translate(663 1093) rotate(-9)">
        <rect x="-116" y="-27" width="232" height="54" rx="27" fill="var(--ink)"/>
        <text class="show-date" x="0" y="4" text-anchor="middle">Saturday, November 11, 2023 → <tspan class="city">Solothurn</tspan></text>
      </g>
    </g>
  </svg>
</main>
</body>
</html>
```